Apartment Hotel
Zielgruppe
Apartment Hotel, verkauf von Hotelzimmer, bzw. Apartments. Für kurzreisende oder Langzeitaufenthalte, für Touristen , Geschäftsleuten, Firmen.
Wir stellen komplette 1 oder 2 Zimmerapartments mit Küche.
www.apartment-hotel-feldburg.de
Aufgabenstellung
modernes Logo , Briefpapier & Visitenkarten , Layout,
Platz für Name/Position: Hotelmanager

```html
<!DOCTYPE html>
<html lang="de">
<head>
<meta charset="utf-8">
<title>Apartment Hotel Feldburg – Geschäftsausstattung</title>
<link href="https://fonts.googleapis.com/css2?family=Source+Sans+3:wght@400;600;700&display=swap" rel="stylesheet">
<style>
  :root {
    --stage-light: #f1f1f1;
    --stage-dark: #5c5c5c;
    --paper: #ffffff;
    --paper-edge: #d3cfd0;
    --ink: #1e1e1e;
    --brand-mist: #cdc8c9;
    --brand-faint: #efeded;
    --card-dark: #45484b;
    --card-light: #d8d3d4;
    --white: #ffffff;
  }
  * { box-sizing: border-box; margin: 0; padding: 0; }
  html, body { width: 1200px; height: 1200px; overflow: hidden; }
  body {
    position: relative;
    font-family: "Source Sans 3", "Segoe UI", sans-serif;
    color: var(--ink);
    background: linear-gradient(155deg, var(--stage-light) 0%, #a9a9a9 48%, var(--stage-dark) 100%);
  }

  /* Wordmarks */
  .wordmark {
    position: absolute;
    font-weight: 400;
    text-transform: uppercase;
    text-align: center;
    white-space: nowrap;
  }
  .wordmark--board { left: 780px; top: 210px; width: 380px; font-size: 56px; letter-spacing: 6px; color: var(--brand-mist); }

  /* Letterhead */
  .letterhead {
    position: absolute;
    left: 34px; top: 142px;
    width: 712px; height: 1008px;
    background: var(--paper);
    border: 9px solid var(--paper-edge);
    box-shadow: 4px 6px 14px rgba(0,0,0,0.35);
    overflow: hidden;
    font-size: 10.5px;
    line-height: 16.8px;
  }
  .letterhead .wordmark--letter { left: 0; top: 80px; width: 100%; font-size: 28px; letter-spacing: 3px; color: var(--brand-mist); }
  .letterhead .backdrop-name {
    position: absolute; right: -20px; bottom: 70px;
    font-size: 96px; letter-spacing: 4px; text-transform: uppercase;
    color: var(--brand-faint); white-space: nowrap;
  }
  .fold-mark { position: absolute; left: 0; width: 12px; height: 1px; background: #9a9a9a; }
  .sender { position: absolute; left: 82px; top: 179px; font-size: 7px; line-height: 9px; color: #444; }
  .recipient { position: absolute; left: 82px; top: 226px; font-size: 11px; line-height: 14.5px; }
  .reference {
    position: absolute; left: 82px; top: 389px; width: 530px;
    display: flex; justify-content: space-between; font-weight: 700; font-size: 10.5px;
  }
  .body-copy { position: absolute; left: 82px; top: 435px; width: 540px; }
  .body-copy p { margin-bottom: 16.8px; }
  .signature { position: absolute; left: 82px; top: 776px; }
  .letter-footer {
    position: absolute; left: 0; bottom: 32px; width: 100%;
    text-align: center; font-size: 9px; line-height: 14px; color: #333;
  }
  .letter-footer .web { font-weight: 700; }

  /* Business cards */
  .card {
    position: absolute;
    border: 7px solid var(--white);
    box-shadow: 3px 5px 12px rgba(0,0,0,0.35);
  }
  .card--front { left: 792px; top: 530px; width: 358px; height: 228px; background: var(--card-dark); }
  .card--front .wordmark { left: 0; top: 82px; width: 100%; font-size: 38px; letter-spacing: 4px; color: var(--white); }
  .card--back { left: 703px; top: 811px; width: 348px; height: 231px; background: var(--card-light); color: var(--white); }
  .card--back .wordmark { left: 14px; top: 84px; width: 130px; font-size: 20px; letter-spacing: 2px; color: var(--white); }
  .card-contact { position: absolute; left: 159px; top: 68px; font-size: 8.5px; line-height: 11px; }
  .card-contact .name { font-size: 13.5px; line-height: 16px; font-weight: 700; }
  .card-contact .role { font-size: 7px; letter-spacing: 1.2px; text-transform: uppercase; margin-bottom: 9px; }
  .card-contact .address { margin-bottom: 8px; }
  .card-contact .lines b { font-weight: 700; }
  .card-contact .web { margin-top: 8px; font-weight: 600; }
</style>
</head>
<body>

  <div class="wordmark wordmark--board">Feldburg</div>

  <article class="letterhead">
    <div class="wordmark wordmark--letter">Feldburg</div>
    <div class="backdrop-name" aria-hidden="true">Feldburg</div>

    <span class="fold-mark" style="top:346px"></span>
    <span class="fold-mark" style="top:435px"></span>

    <div class="sender">Apartment Hotel Feldburg<br>Gartenstraße 14 · 99084 Erfurt</div>

    <address class="recipient" style="font-style:normal">
      Herrn<br>Max Mustermann<br>Musterstraße 12<br>D-34567 Musterstadt
    </address>

    <div class="reference"><span>Ihre Nachricht vom 11.November 2012</span><span>18. November 2014</span></div>

    <div class="body-copy">
      <p>Sehr geehrter Herr Mustermann</p>
      <p>Dies ist ein Blindtext. Bitte beachten Sie den weiteren Inhalt dieses Textes nicht. Es handelt sich tatsächlich,<br>so war mir Gott helfe, nur um einen Blindtext. Ja ja, ich merke schon, Sie können es wohl nicht lassen. Na<br>gut, dann erzähle ich jetzt einen Witz: Wie viele Blondinen braucht man, um eine Glühbirne zu wechseln?</p>
      <p>Fünf, eine, die die Glühbirne hält, und vier, die das Zimmer drehen. Soso, jetzt lachen Sie auch noch, wo<br>ich doch ausdrücklich darauf hingewiesen hatte, den Text überhaupt nicht weiter zu lesen. Manche Leute<br>müssen einfach permanent Regeln brechen. Verdammt noch mal, hier kommt nichts mehr, was auch nur<br>irgendwie von Relevanz wäre.</p>
      <p>Nonsens sozusagen. Nonsens, Nonsens, Nonsens. So was von Nonsens. Nichts wichtiges mehr. Gar nichts.<br>Das Telefonbuch wäre interessanter, da lernt man vielleicht noch nette Leute kennen. Oder an die Wand<br>kucken. Nonsens sozusagen. Nonsens, Nonsens, Nonsens. So was von Nonsens. Nichts wichtiges mehr.<br>Das Telefonbuch wäre interessanter, da lernt man vielleicht noch nette Leute kennen.</p>
      <p>Mit freundlichen Grüßen</p>
    </div>

    <div class="signature">Karin Lehmann<br>Geschäftsführerin</div>

    <footer class="letter-footer">
      Apartment Hotel Feldburg · Gartenstrasse 14 · 99084 Erfurt<br>
      <b>T</b> +49 361 55 20 4-03 · <b>F</b> +49 361 55 20 4-88 · <b>M</b> info@hotel-feldburg.de<br>
      <span class="web">www.apartment-hotel-feldburg.de</span>
    </footer>
  </article>

  <div class="card card--front">
    <div class="wordmark">Feldburg</div>
  </div>

  <div class="card card--back">
    <div class="wordmark">Feldburg</div>
    <div class="card-contact">
      <div class="name">Karin Lehmann</div>
      <div class="role">Hotelmanager</div>
      <div class="address">Apartment Hotel Feldburg<br>Gartenstrasse 14<br>99084 Erfurt</div>
      <div class="lines"><b>T</b> +49(361)5520403<br><b>F</b> +49(361)5520488<br><b>M</b> info@hotel-feldburg.de</div>
      <div class="web">www.apartment-hotel-feldburg.de</div>
    </div>
  </div>

</body>
</html>
```